Book cover for book about ex-wifes

I need a book cover for my new book called "Tidligere brude fra Solen, Stormen og Lindevang" - In english: "Former brides from Sun, Storm and Lindevang" (Hørsholm is a posh city in Denmark).

The book is by men for men about ex-wifes and about how to avoid getting them.
Is it a book from a sexologist and couples therapist to men on how to improve relations.

Men (and curious women)

• Something that indicate three types of ex-wifes

And the author name “Jonas Beltoft”
• Something that says something about relationships, couples and how to stay together (or how to avoid not breaking up)
• No hate

```html
<!DOCTYPE html>
<html lang="da">
<head>
<meta charset="utf-8">
<title>Tidligere brude fra Solen, Stormen og Lindevang — Jonas Beltoft</title>
<link rel="stylesheet" href="https://fonts.googleapis.com/css2?family=Kalam:wght@400;700&family=Open+Sans:wght@400;500&display=swap">
<style>
  :root {
    --page-bg: #e9e9e9;
    --wall: #eeefee;
    --wall-light: #f6f6f5;
    --floor: #c9cac9;
    --floor-dark: #bdbebd;
    --title-orange: #f07a10;
    --ink: #1f1f1f;
    --photo-top: #d6d9df;
    --photo-bottom: #a9b3c4;
  }
  * { margin: 0; padding: 0; box-sizing: border-box; }
  html, body {
    width: 1200px;
    height: 1200px;
    overflow: hidden;
    background: var(--page-bg);
  }
  .stage {
    width: 1200px;
    height: 1200px;
    display: flex;
    align-items: center;
    justify-content: center;
  }
  .book-cover {
    position: relative;
    width: 728px;
    height: 1120px;
    background: linear-gradient(180deg, var(--wall-light) 0%, var(--wall) 80%, var(--floor) 80%, var(--floor-dark) 100%);
    overflow: hidden;
  }
  .title { font-weight: normal; }
  .title-lead {
    position: absolute;
    top: 80px;
    left: 0;
    right: 0;
    text-align: center;
    font-family: "Kalam", cursive;
    font-weight: 700;
    font-size: 104px;
    line-height: 1;
    color: var(--title-orange);
    letter-spacing: -1px;
  }
  .title-rest {
    position: absolute;
    top: 228px;
    left: 0;
    right: 0;
    text-align: center;
    font-family: "Open Sans", sans-serif;
    font-weight: 500;
    font-size: 68px;
    line-height: 72px;
    color: var(--ink);
    letter-spacing: -1px;
  }
  .cover-photo {
    position: absolute;
    left: 135px;
    top: 488px;
    width: 421px;
    height: 500px;
    background: linear-gradient(180deg, var(--photo-top) 0%, var(--photo-bottom) 100%);
  }
  .author-name {
    position: absolute;
    top: 990px;
    left: 0;
    right: 0;
    text-align: center;
    font-family: "Kalam", cursive;
    font-weight: 400;
    font-size: 64px;
    line-height: 1;
    color: var(--ink);
  }
</style>
</head>
<body>
  <main class="stage">
    <article class="book-cover">
      <h1 class="title">
        <span class="title-lead">Tidligere brude</span>
        <span class="title-rest">fra Solen,<br>Stormen<br>og Lindevang</span>
      </h1>
      <div class="cover-photo" role="img" aria-label="Photo of a smiling young couple sitting on the floor against a white wall, the man pointing upward while both look up"></div>
      <p class="author-name">Jonas Beltoft</p>
    </article>
  </main>
</body>
</html>
```